Corvane Tea range - labels for a range of teas.

Our company name is Corvane Tea Company - based in Melbourne, Australia. We have a current logo project with Draft Plaza.

We offer a range of top quality teas - black, green, white, oolongs, herbals, flavoured teas. From Japan, Assam, Darjeeling, Ceylon, Africa and elsewhere. The very best loose teas, and some pyramid tea bags too.

We cover some blends : English Breakfast, African Breakfast, Ceylon Breakfast, Earl Grey amongst them.

And herbal variants: lemon grass and ginger, chamomile, peppermint, rooibos and chilli.

And fruit teas.... and flavoured teas like vanilla, peach and raspberry.

We aim to occupy a modern, contemporary, sophisticated and global space.... but we can be funky too, especially with the fruit and herbal offers. Quality is paramount ! We do not aim to have the biggest range of teas, but we are very particular. And we source directly from origin.... fresh quality teas.

Would lean towards black teas being on a black background label, green teas on a green background, white etas on a white background, herbals maybe on a straw or suitable background, and flavoured teas on a specific background colour too....maybe fuschia? Violet ? But colourful is key.

The panel should indicate teas being Loose or Pyramid bags. And the nett weight should be shown.... Loose could be for example 75 gr, 125 gr 250 gr etc.. And pyramids would show the number of pyramids and weight, example 20 x Pyramids 50 gr
50 Pyramids 150 gr etc.

And 'Corvane Teas' or 'Corvane Tea Company' should be on the panel too. Melbourne can appear as well if it gels with the total look.

There will need to be 2 lines - in order or juxtaposed, doesn't matter - showing the origin and 'mark' and grade. Example being:
Ceylon
Wendrick Pekoe

or

Darjeeling
Morvani TGFOP1

or

China
Jasmine Leaf

We just need templates to cover the different types of tea - black, green, white, herbal, flavoured - as there are too many (and changing) types of tea in the range .

Any questions...please ask...

Thanks

Reason: Needs to have alater deadline than the current Logo Project associated with the same Corvane Tea Company start up.

Target Market(s)

Sophisticated. Real tea lovers. Discriminating tastes.

Weight

Font styles to use
Sans Serif

Requirements
Must have
• Sophisticated
Cool
Premium quality branding
Bold
Uber modern
Nice to have
• BOLD text.....
Cool fonts....
Pretty bold and minimalist - ultra modern if possible....uber modern
Bright colours and use of black and white..... Not really into pastels etc..

Lots of black colour too is a likely plus
Should not have
• Frilly stuff

```html
<!DOCTYPE html>
<html lang="en">
<head>
<meta charset="utf-8">
<title>Corvane Tea Company – Tea Range Labels</title>
<link rel="stylesheet" href="https://fonts.googleapis.com/css2?family=Pacifico&family=Quicksand:wght@700&display=swap">
<style>
  :root {
    --page: #ffffff;
    --black: #141414;
    --green: #b5bcb5;
    --white-tea: #fbf1d6;
    --white-ink: #b4b4b4;
    --oolong: #a44f4c;
    --herbal: #dd9d58;
    --flavoured: #7cb2c1;
    --paper: #ffffff;
  }
  * { margin: 0; padding: 0; box-sizing: border-box; }
  html, body { width: 1200px; height: 1148px; overflow: hidden; background: var(--page); }
  .sheet { position: relative; width: 1200px; height: 1148px; }

  .label {
    position: absolute;
    width: 370px;
    height: 524px;
    color: var(--paper);
    font-family: "Quicksand", sans-serif;
    font-weight: 700;
    text-align: center;
  }
  .label--black { left: 28px; top: 23px; --tone: var(--black); }
  .label--green { left: 414px; top: 23px; --tone: var(--green); }
  .label--white { left: 804px; top: 23px; --tone: var(--white-tea); color: var(--white-ink); }
  .label--oolong { left: 28px; top: 600px; --tone: var(--oolong); }
  .label--herbal { left: 414px; top: 600px; --tone: var(--herbal); }
  .label--flavoured { left: 804px; top: 600px; --tone: var(--flavoured); }

  .label__shape { position: absolute; inset: 0; width: 370px; height: 524px; }
  .label__outline { fill: none; stroke: var(--tone); stroke-width: 5; }
  .label__inner { fill: none; stroke: var(--paper); stroke-width: 2; }

  .label__cup {
    position: absolute; left: 157px; top: 84px; width: 58px; height: 58px;
    fill: none; stroke: currentColor; stroke-width: 2.6; stroke-linecap: round; stroke-linejoin: round;
  }
  .label--white .label__cup { stroke: var(--white-ink); }

  .label__name {
    position: absolute; left: 0; right: 0; top: 236px;
    font-family: "Pacifico", cursive;
    font-weight: 400;
    font-size: 52px;
    line-height: 1;
    white-space: nowrap;
    letter-spacing: -0.5px;
  }
  .label__origin, .label__grade, .label__company {
    position: absolute; left: 0; right: 0;
    font-size: 17px; line-height: 1;
  }
  .label__origin { top: 325px; }
  .label__grade { top: 351px; }
  .label__company { top: 379px; }
  .label__city {
    position: absolute; right: 88px; top: 402px;
    font-size: 11.5px; line-height: 1;
  }
  .label__weight {
    position: absolute; left: 0; right: 0; top: 424px;
    font-size: 12.5px; line-height: 1;
  }
  .label__weight--pyramid { right: 48px; }
</style>
</head>
<body>
<main class="sheet">

  <!-- Black -->
  <article class="label label--black">
    <svg class="label__shape" viewBox="0 0 370 524">
      <defs>
        <linearGradient id="wash-black" x1="0" y1="1" x2="1" y2="0">
          <stop offset="0" stop-color="#141414"/>
          <stop offset="0.45" stop-color="#4a4a4a"/>
          <stop offset="0.8" stop-color="#e8e8e8"/>
          <stop offset="1" stop-color="#ffffff"/>
        </linearGradient>
      </defs>
      <polygon role="img" aria-label="Charcoal watercolour wash fading to white" points="0,0 370,0 370,403 185,524 0,403" fill="url(#wash-black)"/>
      <polygon class="label__inner" points="9,9 361,9 361,398 185,512 9,398"/>
      <polygon class="label__outline" points="2.5,2.5 367.5,2.5 367.5,402 185,521 2.5,402"/>
    </svg>
    <svg class="label__cup" viewBox="0 0 58 58"><path d="M14 16h26v14c0 8-6 13-13 13s-13-5-13-13z"/><path d="M40 20h4a5 5 0 0 1 0 10h-4"/><ellipse cx="28" cy="47" rx="24" ry="6"/><path d="M18 22c5 2 13 2 18 0"/></svg>
    <h2 class="label__name">Black Tea</h2>
    <p class="label__origin">First Line.</p>
    <p class="label__grade">Second Line.</p>
    <p class="label__company">Corvane Tea Company.</p>
    <p class="label__city">Melbourne.</p>
    <p class="label__weight label__weight--pyramid">50 Pyramids 150g</p>
  </article>

  <!-- Green -->
  <article class="label label--green">
    <svg class="label__shape" viewBox="0 0 370 524">
      <defs>
        <linearGradient id="wash-green" x1="0" y1="1" x2="1" y2="0">
          <stop offset="0" stop-color="#a9b1a9"/>
          <stop offset="0.5" stop-color="#c5cbc4"/>
          <stop offset="0.85" stop-color="#f4f5f3"/>
          <stop offset="1" stop-color="#ffffff"/>
        </linearGradient>
      </defs>
      <polygon role="img" aria-label="Sage green watercolour wash fading to white" points="0,0 370,0 370,403 185,524 0,403" fill="url(#wash-green)"/>
      <polygon class="label__inner" points="9,9 361,9 361,398 185,512 9,398"/>
      <polygon class="label__outline" points="2.5,2.5 367.5,2.5 367.5,402 185,521 2.5,402"/>
    </svg>
    <svg class="label__cup" viewBox="0 0 58 58"><path d="M14 16h26v14c0 8-6 13-13 13s-13-5-13-13z"/><path d="M40 20h4a5 5 0 0 1 0 10h-4"/><ellipse cx="28" cy="47" rx="24" ry="6"/><path d="M18 22c5 2 13 2 18 0"/></svg>
    <h2 class="label__name">Green Tea</h2>
    <p class="label__origin">First Line.</p>
    <p class="label__grade">Second Line.</p>
    <p class="label__company">Corvane Tea Company.</p>
    <p class="label__city">Melbourne.</p>
    <p class="label__weight">250g</p>
  </article>

  <!-- White -->
  <article class="label label--white">
    <svg class="label__shape" viewBox="0 0 370 524">
      <defs>
        <linearGradient id="wash-white" x1="0" y1="1" x2="1" y2="0">
          <stop offset="0" stop-color="#faefd0"/>
          <stop offset="0.6" stop-color="#fcf5e2"/>
          <stop offset="1" stop-color="#fffdf6"/>
        </linearGradient>
      </defs>
      <polygon role="img" aria-label="Pale cream watercolour wash" points="0,0 370,0 370,403 185,524 0,403" fill="url(#wash-white)"/>
      <polygon class="label__inner" points="9,9 361,9 361,398 185,512 9,398"/>
      <polygon class="label__outline" points="2.5,2.5 367.5,2.5 367.5,402 185,521 2.5,402"/>
    </svg>
    <svg class="label__cup" viewBox="0 0 58 58"><path d="M14 16h26v14c0 8-6 13-13 13s-13-5-13-13z"/><path d="M40 20h4a5 5 0 0 1 0 10h-4"/><ellipse cx="28" cy="47" rx="24" ry="6"/><path d="M18 22c5 2 13 2 18 0"/></svg>
    <h2 class="label__name">White Tea</h2>
    <p class="label__origin">First Line.</p>
    <p class="label__grade">Second Line.</p>
    <p class="label__company">Corvane Tea Company.</p>
    <p class="label__city">Melbourne.</p>
    <p class="label__weight">250g</p>
  </article>

  <!-- Oolong -->
  <article class="label label--oolong">
    <svg class="label__shape" viewBox="0 0 370 524">
      <defs>
        <linearGradient id="wash-oolong" x1="0" y1="1" x2="1" y2="0">
          <stop offset="0" stop-color="#a44f4c"/>
          <stop offset="0.45" stop-color="#c68a88"/>
          <stop offset="0.8" stop-color="#f2e4e3"/>
          <stop offset="1" stop-color="#ffffff"/>
        </linearGradient>
      </defs>
      <polygon role="img" aria-label="Brick red watercolour wash fading to white" points="0,0 370,0 370,403 185,524 0,403" fill="url(#wash-oolong)"/>
      <polygon class="label__inner" points="9,9 361,9 361,398 185,512 9,398"/>
      <polygon class="label__outline" points="2.5,2.5 367.5,2.5 367.5,402 185,521 2.5,402"/>
    </svg>
    <svg class="label__cup" viewBox="0 0 58 58"><path d="M14 16h26v14c0 8-6 13-13 13s-13-5-13-13z"/><path d="M40 20h4a5 5 0 0 1 0 10h-4"/><ellipse cx="28" cy="47" rx="24" ry="6"/><path d="M18 22c5 2 13 2 18 0"/></svg>
    <h2 class="label__name">Oolongs Tea</h2>
    <p class="label__origin">First Line.</p>
    <p class="label__grade">Second Line.</p>
    <p class="label__company">Corvane Tea Company.</p>
    <p class="label__city">Melbourne.</p>
    <p class="label__weight">250g</p>
  </article>

  <!-- Herbal -->
  <article class="label label--herbal">
    <svg class="label__shape" viewBox="0 0 370 524">
      <defs>
        <linearGradient id="wash-herbal" x1="0" y1="1" x2="1" y2="0">
          <stop offset="0" stop-color="#dd9d58"/>
          <stop offset="0.45" stop-color="#e9bb89"/>
          <stop offset="0.8" stop-color="#f9ece0"/>
          <stop offset="1" stop-color="#ffffff"/>
        </linearGradient>
      </defs>
      <polygon role="img" aria-label="Straw orange watercolour wash fading to white" points="0,0 370,0 370,403 185,524 0,403" fill="url(#wash-herbal)"/>
      <polygon class="label__inner" points="9,9 361,9 361,398 185,512 9,398"/>
      <polygon class="label__outline" points="2.5,2.5 367.5,2.5 367.5,402 185,521 2.5,402"/>
    </svg>
    <svg class="label__cup" viewBox="0 0 58 58"><path d="M14 16h26v14c0 8-6 13-13 13s-13-5-13-13z"/><path d="M40 20h4a5 5 0 0 1 0 10h-4"/><ellipse cx="28" cy="47" rx="24" ry="6"/><path d="M18 22c5 2 13 2 18 0"/></svg>
    <h2 class="label__name">Herbal Tea</h2>
    <p class="label__origin">First Line.</p>
    <p class="label__grade">Second Line.</p>
    <p class="label__company">Corvane Tea Company.</p>
    <p class="label__city">Melbourne.</p>
    <p class="label__weight label__weight--pyramid">50 Pyramids 150g</p>
  </article>

  <!-- Flavoured -->
  <article class="label label--flavoured">
    <svg class="label__shape" viewBox="0 0 370 524">
      <defs>
        <linearGradient id="wash-flavoured" x1="0" y1="1" x2="1" y2="0">
          <stop offset="0" stop-color="#7cb2c1"/>
          <stop offset="0.45" stop-color="#a6cbd6"/>
          <stop offset="0.8" stop-color="#e8f2f5"/>
          <stop offset="1" stop-color="#ffffff"/>
        </linearGradient>
      </defs>
      <polygon role="img" aria-label="Soft blue watercolour wash fading to white" points="0,0 370,0 370,403 185,524 0,403" fill="url(#wash-flavoured)"/>
      <polygon class="label__inner" points="9,9 361,9 361,398 185,512 9,398"/>
      <polygon class="label__outline" points="2.5,2.5 367.5,2.5 367.5,402 185,521 2.5,402"/>
    </svg>
    <svg class="label__cup" viewBox="0 0 58 58"><path d="M14 16h26v14c0 8-6 13-13 13s-13-5-13-13z"/><path d="M40 20h4a5 5 0 0 1 0 10h-4"/><ellipse cx="28" cy="47" rx="24" ry="6"/><path d="M18 22c5 2 13 2 18 0"/></svg>
    <h2 class="label__name">Flavoured Tea</h2>
    <p class="label__origin">First Line.</p>
    <p class="label__grade">Second Line.</p>
    <p class="label__company">Corvane Tea Company.</p>
    <p class="label__city">Melbourne.</p>
    <p class="label__weight">250g</p>
  </article>

</main>
</body>
</html>
```